Business card design needed

We need a buisness card design to suit our buisness "Maple Parcel", a company on the south coast of Australia, a wholesale greeting card and gift wrap buisness. We are open to different colour options possibly some pastels. A card that got my attention was'the ''hoofnotes.com.au'' buisness card. I liked the colour scheme, layout, and the use of a cartoon image, but am also open to all ideas.

Industry/Entity Type

Business

Contact Information for Business Card

Maple Parcel Unit 37 / 18 Banksia ave West Torrin 2563 ph 0244879351 fax 0244879352 Colin Madsey email maple.parcel@postvale.com

```html
<!DOCTYPE html>
<html lang="en">
<head>
<meta charset="utf-8">
<title>Maple Parcel – Business Card</title>
<link rel="stylesheet" href="https://fonts.googleapis.com/css2?family=Exo+2:wght@400;500;600;700&display=swap">
<style>
  :root {
    --teal: #0f8d82;
    --teal-deep: #0a6c64;
    --teal-light: #1aa596;
    --cream: #f1efe7;
    --cream-shade: #e2ded2;
    --gold: #c7a46a;
    --gold-light: #e8d7b4;
    --backdrop: #e7e4df;
    --white: #ffffff;
  }
  * { box-sizing: border-box; margin: 0; padding: 0; }
  html, body { width: 1200px; height: 880px; overflow: hidden; }
  body {
    background: var(--backdrop);
    font-family: "Exo 2", "Segoe UI", sans-serif;
    position: relative;
  }
  .card {
    position: absolute;
    width: 700px;
    height: 400px;
    border-radius: 4px;
    overflow: hidden;
    box-shadow: 0 10px 28px rgba(0, 0, 0, 0.18);
  }
  .card-art { position: absolute; inset: 0; width: 100%; height: 100%; }

  /* Back card: contact side */
  .card--contact {
    left: 440px;
    top: 30px;
    background: linear-gradient(160deg, var(--teal-light) 0%, var(--teal) 45%, var(--teal-deep) 100%);
  }
  .contact-block {
    position: absolute;
    right: 48px;
    top: 146px;
    width: 360px;
    color: var(--white);
    text-align: right;
  }
  .contact-name {
    font-size: 40px;
    font-weight: 700;
    letter-spacing: 0.5px;
    line-height: 1;
    padding-bottom: 14px;
    border-bottom: 1.5px solid rgba(255, 255, 255, 0.75);
  }
  .contact-list { list-style: none; padding: 9px 0; }
  .contact-list--address { border-top: 1.5px solid rgba(255, 255, 255, 0.75); }
  .contact-item {
    display: flex;
    justify-content: flex-end;
    align-items: center;
    gap: 12px;
    font-size: 19px;
    font-weight: 400;
    line-height: 1.45;
  }
  .contact-item svg { width: 18px; height: 18px; flex: none; }
  .contact-item--bare { padding-right: 30px; }

  /* Front card: brand side */
  .card--brand {
    left: 60px;
    top: 450px;
    background: var(--cream);
  }
  .brand-mark {
    position: absolute;
    left: 200px;
    top: 210px;
    display: flex;
    align-items: center;
    gap: 16px;
    color: var(--teal);
  }
  .brand-square { width: 30px; height: 30px; background: var(--teal); }
  .brand-name { font-size: 50px; font-weight: 600; line-height: 1; }
  .brand-services {
    position: absolute;
    left: 26px;
    bottom: 30px;
    color: var(--teal);
    font-size: 19.5px;
    font-weight: 500;
    letter-spacing: 0.6px;
    white-space: nowrap;
  }
</style>
</head>
<body>

<section class="card card--contact" aria-label="Business card, contact side">
  <svg class="card-art" viewBox="0 0 700 400" aria-hidden="true">
    <defs>
      <linearGradient id="ribbonSheen" x1="0" y1="1" x2="1" y2="0">
        <stop offset="0" stop-color="var(--cream-shade)"/>
        <stop offset="0.5" stop-color="var(--white)"/>
        <stop offset="1" stop-color="var(--cream-shade)"/>
      </linearGradient>
    </defs>
    <polygon points="0,0 700,0 700,70 0,250" fill="var(--cream)"/>
    <polygon points="0,200 700,25 700,70 0,250" fill="url(#ribbonSheen)"/>
    <line x1="0" y1="200" x2="700" y2="25" stroke="var(--gold)" stroke-width="2.5"/>
    <line x1="0" y1="250" x2="700" y2="70" stroke="var(--gold)" stroke-width="2.5"/>
  </svg>
  <svg class="card-art" viewBox="0 0 700 400" role="img" aria-label="Illustration of a satin gift bow with gold edging">
    <defs>
      <radialGradient id="bowTone" cx="0.5" cy="0.45" r="0.55">
        <stop offset="0" stop-color="#ffffff"/>
        <stop offset="0.6" stop-color="#ece6d8"/>
        <stop offset="1" stop-color="#ece6d8" stop-opacity="0"/>
      </radialGradient>
    </defs>
    <ellipse cx="205" cy="115" rx="125" ry="90" fill="url(#bowTone)"/>
  </svg>

  <div class="contact-block">
    <p class="contact-name">Delia Norwood</p>
    <ul class="contact-list">
      <li class="contact-item">0244.879.351
        <svg viewBox="0 0 18 18" aria-hidden="true"><rect x="5" y="1.5" width="8" height="15" rx="1.6" fill="none" stroke="currentColor" stroke-width="1.6"/><circle cx="9" cy="13.5" r="1" fill="currentColor"/></svg>
      </li>
      <li class="contact-item">0244.879.352
        <svg viewBox="0 0 18 18" aria-hidden="true"><rect x="4.5" y="2" width="9" height="5" fill="none" stroke="currentColor" stroke-width="1.5"/><rect x="1.5" y="7" width="15" height="7" rx="1.2" fill="currentColor"/><rect x="4.5" y="12" width="9" height="4.5" fill="var(--white)" stroke="currentColor" stroke-width="1.2"/></svg>
      </li>
      <li class="contact-item">maple.parcel@postvale.com
        <svg viewBox="0 0 18 18" aria-hidden="true"><rect x="1.5" y="4" width="15" height="10" rx="1" fill="none" stroke="currentColor" stroke-width="1.5"/><polyline points="1.8,4.5 9,10 16.2,4.5" fill="none" stroke="currentColor" stroke-width="1.5"/></svg>
      </li>
    </ul>
    <ul class="contact-list contact-list--address">
      <li class="contact-item contact-item--bare">Unit 37 / 18 Banksia Ave</li>
      <li class="contact-item">West Torrin 2563
        <svg viewBox="0 0 18 18" aria-hidden="true"><path d="M9 1.5a5.5 5.5 0 0 0-5.5 5.5c0 4.2 5.5 9.5 5.5 9.5s5.5-5.3 5.5-9.5A5.5 5.5 0 0 0 9 1.5z" fill="currentColor"/><circle cx="9" cy="7" r="2.1" fill="var(--teal)"/></svg>
      </li>
    </ul>
  </div>
</section>

<section class="card card--brand" aria-label="Business card, brand side">
  <svg class="card-art" viewBox="0 0 700 400" aria-hidden="true">
    <defs>
      <linearGradient id="cornerTeal" x1="0" y1="0" x2="1" y2="1">
        <stop offset="0" stop-color="var(--teal-light)"/>
        <stop offset="1" stop-color="var(--teal-deep)"/>
      </linearGradient>
      <linearGradient id="bandSheen" x1="0" y1="1" x2="1" y2="0">
        <stop offset="0" stop-color="var(--gold-light)"/>
        <stop offset="0.5" stop-color="var(--white)"/>
        <stop offset="1" stop-color="var(--gold-light)"/>
      </linearGradient>
    </defs>
    <polygon points="0,0 330,0 0,200" fill="url(#cornerTeal)"/>
    <polygon points="330,0 385,0 0,235 0,200" fill="url(#bandSheen)"/>
    <line x1="330" y1="0" x2="0" y2="200" stroke="var(--gold)" stroke-width="2.5"/>
    <line x1="385" y1="0" x2="0" y2="235" stroke="var(--gold)" stroke-width="2.5"/>
  </svg>

  <div class="brand-mark">
    <span class="brand-square" aria-hidden="true"></span>
    <span class="brand-name">Maple Parcel</span>
  </div>
  <p class="brand-services">greeting cards • gift wrap • ribbon • bows • celo • tissue paper</p>
</section>

</body>
</html>
```